Design a CD Cover For Baby Music and Lullabies To Appear on Tunvale Store etc.

Please read this brief before you design. Otherwise you will be wasting your time.

I need a cd cover for music albums which will appear on streaming sites such as Tunvale Store Melodrift, Vimtro etc. for the brand Snug Cradle Tunes. The thumbnails are quite small so the text needs to be quite large.

I need a design if possible, in which I can simply alter the title of the album and the baby picture so that each album has a different cover but works with the branding.

You can check out the Snug Cradle Tunes on the Tunvale store.
https://play.melodriftaudio.net/artist/8kQ3xTnRwLpV27hYbMdZc4

I made those covers and I really don't like them at all! As you can tell I am not a graphic designer. Ha.

Please help me with a modern, eye catching and cute design that will work across the brand now and in the future. The SCT logo and the name Snug Cradle Tunes is the only thing that needs to be used somewhere in the design.

Please use the title

Gentle Static Hums For Nap Time Series A

for this first album.
(White noise sounds are hair dryers, vacuum cleaners, fans, wind, rain, the sea, white noise, pink noise, brown noise etc. )

Here is an example of album covers which are coherent. A style like this without the over the top text would be good. But don't copy these!
https://play.melodriftaudio.net/artist/9TqWmLx5Rb2Hn7KcVpYe1z

Target Market(s)

Parents of babies.

Font styles to use
Serif
Sans Serif

Colors

Designer to choose colors to be used in the design.

Requirements
Must have
• Large font so it can been seen in the melodrift thumbnail. A photo of a baby. Please take a look at the melodrift and tunvale stores. The Snug Cradle Tunes logo.
• Album Title
• Gentle Static Hums For Nap Time Series A

```html
<!DOCTYPE html>
<html lang="en">
<head>
<meta charset="utf-8">
<title>Snug Cradle Tunes – Gentle Static Hums For Nap Time, Series A</title>
<link rel="stylesheet" href="https://fonts.googleapis.com/css2?family=Allura&family=Cormorant+Garamond:wght@500&family=Montserrat:wght@500;600&display=swap">
<style>
  :root {
    --ink: #4a4a4c;
    --ink-soft: #5c5c5e;
    --band: rgba(255, 255, 255, 0.8);
    --band-line: rgba(175, 165, 165, 0.5);
    --badge: #ffffff;
    --star: #e98c9a;
    --skin: #e9b9a0;
    --skin-deep: #d99a80;
  }
  * { box-sizing: border-box; margin: 0; padding: 0; }
  html, body {
    width: 1200px;
    height: 1200px;
    overflow: hidden;
    background: #ffffff;
  }
  .cover-sheet {
    display: grid;
    grid-template-columns: 600px 600px;
    grid-template-rows: 600px 600px;
    width: 1200px;
    height: 1200px;
  }
  .cover {
    position: relative;
    width: 600px;
    height: 600px;
    overflow: hidden;
  }
  .cover__photo {
    position: absolute;
    inset: 0;
  }
  .cover--cream .cover__photo {
    background:
      radial-gradient(ellipse 260px 150px at 300px 290px, var(--skin) 0%, rgba(233,185,160,0.7) 55%, rgba(233,185,160,0) 100%),
      radial-gradient(ellipse 200px 130px at 390px 190px, #fbf8f2 0%, rgba(251,248,242,0) 100%),
      linear-gradient(180deg, #ece7df 0%, #efe9e1 60%, #f6f1ec 100%);
  }
  .cover--blush .cover__photo {
    background:
      radial-gradient(ellipse 230px 150px at 360px 250px, var(--skin) 0%, rgba(233,185,160,0.65) 55%, rgba(233,185,160,0) 100%),
      radial-gradient(ellipse 260px 140px at 330px 360px, #f2bfcd 0%, rgba(242,191,205,0) 100%),
      radial-gradient(ellipse 200px 200px at 560px 120px, #c8bfb5 0%, rgba(200,191,181,0) 100%),
      linear-gradient(180deg, #e5d3e3 0%, #ece0ea 100%);
  }
  .cover--sky .cover__photo {
    background:
      radial-gradient(ellipse 180px 180px at 340px 300px, #f0c3a8 0%, rgba(240,195,168,0.6) 55%, rgba(240,195,168,0) 100%),
      radial-gradient(ellipse 330px 260px at 260px 300px, #d9bb9c 0%, rgba(217,187,156,0.5) 60%, rgba(217,187,156,0) 100%),
      linear-gradient(180deg, #dde4ee 0%, #eee8e2 100%);
  }
  .cover--mint .cover__photo {
    background:
      radial-gradient(ellipse 220px 120px at 340px 250px, var(--skin) 0%, rgba(233,185,160,0.7) 55%, rgba(233,185,160,0) 100%),
      radial-gradient(ellipse 160px 90px at 220px 200px, #6e4e3a 0%, rgba(110,78,58,0) 100%),
      linear-gradient(180deg, #bfe2dc 0%, #c7e3dd 35%, #c99a72 60%, #b7825a 75%, #e8ddd2 100%);
  }
  .brand-badge {
    position: absolute;
    top: 28px;
    left: 50%;
    width: 96px;
    height: 96px;
    margin-left: -48px;
    border-radius: 50%;
    background: var(--badge);
    display: flex;
    align-items: center;
    justify-content: center;
    text-align: center;
    font-family: "Montserrat", sans-serif;
    font-weight: 600;
    font-size: 12px;
    line-height: 1.25;
    letter-spacing: 1.5px;
    text-transform: uppercase;
    color: var(--ink);
  }
  .title-band {
    position: absolute;
    left: 0;
    right: 0;
    bottom: 0;
    height: 172px;
    background: var(--band);
    text-align: center;
  }
  .title-band::before {
    content: "";
    position: absolute;
    inset: 6px 8px 4px 8px;
    border: 1px solid var(--band-line);
  }
  .album-title {
    position: relative;
    padding-top: 26px;
    font-family: "Allura", cursive;
    font-weight: 400;
    font-size: 52px;
    line-height: 1;
    color: var(--ink);
  }
  .album-subtitle {
    position: relative;
    margin-top: 2px;
    font-family: "Cormorant Garamond", serif;
    font-weight: 500;
    font-size: 26px;
    letter-spacing: 4px;
    color: var(--ink-soft);
  }
  .album-star {
    position: relative;
    display: block;
    margin: 8px auto 0;
    width: 14px;
    height: 14px;
  }
  .album-series {
    position: relative;
    margin-top: 8px;
    font-family: "Montserrat", sans-serif;
    font-weight: 500;
    font-size: 11px;
    letter-spacing: 3px;
    text-transform: uppercase;
    color: var(--ink);
  }
</style>
</head>
<body>
<main class="cover-sheet">

  <section class="cover cover--cream">
    <div class="cover__photo" role="img" aria-label="Photo of a sleeping newborn in a white knitted bonnet with a pink flower, soft cream background with light bokeh"></div>
    <div class="brand-badge">Snug<br>Cradle<br>Tunes</div>
    <div class="title-band">
      <h1 class="album-title">Gentle Static Hums</h1>
      <p class="album-subtitle">for nap time</p>
      <svg class="album-star" viewBox="0 0 24 24" aria-hidden="true"><polygon points="12,2 15,9 22,9.5 16.5,14 18.5,21.5 12,17.5 5.5,21.5 7.5,14 2,9.5 9,9" fill="var(--star)"/></svg>
      <p class="album-series">Series A</p>
    </div>
  </section>

  <section class="cover cover--blush">
    <div class="cover__photo" role="img" aria-label="Photo of a newborn sleeping curled on pink feathers in a woven nest, lilac background with light bokeh"></div>
    <div class="brand-badge">Snug<br>Cradle<br>Tunes</div>
    <div class="title-band">
      <h2 class="album-title">Gentle Static Hums</h2>
      <p class="album-subtitle">for nap time</p>
      <svg class="album-star" viewBox="0 0 24 24" aria-hidden="true"><polygon points="12,2 15,9 22,9.5 16.5,14 18.5,21.5 12,17.5 5.5,21.5 7.5,14 2,9.5 9,9" fill="var(--star)"/></svg>
      <p class="album-series">Series A</p>
    </div>
  </section>

  <section class="cover cover--sky">
    <div class="cover__photo" role="img" aria-label="Photo of a sleeping newborn in a beige knitted bunny hat holding a knitted toy, pale blue background with light bokeh"></div>
    <div class="brand-badge">Snug<br>Cradle<br>Tunes</div>
    <div class="title-band">
      <h2 class="album-title">Gentle Static Hums</h2>
      <p class="album-subtitle">for nap time</p>
      <svg class="album-star" viewBox="0 0 24 24" aria-hidden="true"><polygon points="12,2 15,9 22,9.5 16.5,14 18.5,21.5 12,17.5 5.5,21.5 7.5,14 2,9.5 9,9" fill="var(--star)"/></svg>
      <p class="album-series">Series A</p>
    </div>
  </section>

  <section class="cover cover--mint">
    <div class="cover__photo" role="img" aria-label="Photo of a sleeping newborn in a wicker basket with a parent's hand resting on its head, mint background with light bokeh"></div>
    <div class="brand-badge">Snug<br>Cradle<br>Tunes</div>
    <div class="title-band">
      <h2 class="album-title">Gentle Static Hums</h2>
      <p class="album-subtitle">for nap time</p>
      <svg class="album-star" viewBox="0 0 24 24" aria-hidden="true"><polygon points="12,2 15,9 22,9.5 16.5,14 18.5,21.5 12,17.5 5.5,21.5 7.5,14 2,9.5 9,9" fill="var(--star)"/></svg>
      <p class="album-series">Series A</p>
    </div>
  </section>

</main>
</body>
</html>
```